Cedar Harbor Business Cards For New Startup

I am looking for you to design some business cards for a new startup https://cedarharborhub.com. I have supplied logo, brand guidelines and our signatures as a guide.

We need this to reflect the brand guidelines and the website for brand consistency,

What is Cedar Harbor?

Mallorca's Business Growth Community
Join your new business community full of passionate entrepreneurs who
love to solve problems and help each other grow together!

Any questions you can ask.

Target Market(s)

Business to Business

Contact Information for Business Card

These are attached (signatures) to the job

Font styles to use
Other font styles liked:
• Open Sans

Requirements
Must have
• Match design guidelines
Nice to have
• Photos of our faces so people remember us

```html
<!DOCTYPE html>
<html lang="en">
<head>
<meta charset="utf-8">
<title>Cedar Harbor Business Cards</title>
<link rel="stylesheet" href="https://fonts.googleapis.com/css2?family=Open+Sans:wght@400;600;700&display=swap">
<style>
  :root {
    --olive: #6b6f30;
    --olive-dark: #5a5e27;
    --olive-pattern: #777b3c;
    --paper: #ffffff;
    --ink: #3a3a3a;
    --rule: #4a4a4a;
    --bg-top: #98a079;
    --bg-bottom: #5f6532;
  }
  * { box-sizing: border-box; margin: 0; padding: 0; }
  html, body { width: 1200px; height: 895px; overflow: hidden; }
  body {
    font-family: "Open Sans", Arial, sans-serif;
    background: linear-gradient(180deg, var(--bg-top), var(--bg-bottom));
    display: flex; flex-direction: column; align-items: center; justify-content: center;
    gap: 40px;
  }
  .card {
    width: 680px; height: 390px; position: relative;
    box-shadow: 0 10px 24px rgba(0,0,0,.3);
  }
  .card-back { background: var(--olive); display: flex; align-items: center; justify-content: center; }
  .card-back .pattern-area {
    position: absolute; inset: 0;
    background: radial-gradient(circle at 50% 50%, var(--olive-pattern), var(--olive) 70%);
    opacity: .6;
  }
  .brand { display: flex; align-items: center; gap: 16px; position: relative; }
  .brand-mark { width: 56px; height: 56px; border-radius: 50%; border: 2.5px solid currentColor; }
  .brand-name { font-weight: 700; font-size: 40px; letter-spacing: 1px; text-transform: uppercase; }
  .card-back .brand { color: var(--paper); }
  .card-front { background: var(--paper); color: var(--ink); }
  .card-front .brand { position: absolute; top: 48px; left: 300px; color: var(--olive); }
  .card-front .brand-name { font-size: 34px; }
  .card-front .brand-mark { width: 48px; height: 48px; }
  .portrait {
    position: absolute; left: 40px; top: 70px; width: 190px; height: 170px;
    background: linear-gradient(135deg, #c9b7a8, #e8d3a0 50%, #8d7f86);
  }
  .person { position: absolute; left: 40px; top: 252px; }
  .person-name { font-size: 28px; font-weight: 700; color: var(--olive); line-height: 1.1; }
  .person-role { font-size: 15px; color: var(--ink); margin-top: 2px; }
  .contact { position: absolute; left: 40px; top: 322px; width: 330px; border-top: 1.5px solid var(--rule); padding-top: 8px; font-size: 15px; }
  .contact li { list-style: none; display: flex; align-items: center; gap: 10px; line-height: 1.5; }
  .contact svg { width: 14px; height: 14px; fill: none; stroke: var(--olive); stroke-width: 1.6; }
  .accent { color: var(--olive); }
  .social { position: absolute; right: 40px; top: 210px; display: flex; gap: 8px; }
  .social span { width: 28px; height: 28px; border-radius: 50%; border: 1.5px solid var(--olive); }
  .web { position: absolute; right: 40px; top: 250px; width: 250px; border-top: 1.5px solid var(--rule); padding-top: 10px; font-size: 15px; display: flex; justify-content: flex-end; align-items: center; gap: 8px; }
  .web svg { width: 14px; height: 14px; fill: none; stroke: var(--olive); stroke-width: 1.5; }
  .card-front::after { content: ""; position: absolute; left: 0; right: 0; bottom: 0; height: 6px; background: var(--olive); }
</style>
</head>
<body>
  <section class="card card-back">
    <div class="pattern-area" role="img" aria-label="Repeating outline brand pattern across the olive card back"></div>
    <div class="brand">
      <span class="brand-mark"></span>
      <span class="brand-name">Cedar Harbor</span>
    </div>
  </section>

  <section class="card card-front">
    <div class="brand">
      <span class="brand-mark"></span>
      <span class="brand-name">Cedar Harbor</span>
    </div>
    <div class="portrait" role="img" aria-label="Portrait photo of the card holder"></div>
    <div class="person">
      <p class="person-name">Helena Marsh</p>
      <p class="person-role">Relationship Director | Cedar Harbor</p>
    </div>
    <ul class="contact">
      <li><svg viewBox="0 0 14 14"><rect x="3.5" y="1" width="7" height="12" rx="1.2"/><line x1="6" y1="11" x2="8" y2="11"/></svg>+44 7700 900 123</li>
      <li><svg viewBox="0 0 14 14"><rect x="1" y="3" width="12" height="8"/><polyline points="1,3 7,8 13,3"/></svg>hm@<span class="accent">cedarharborhub</span>.com</li>
    </ul>
    <div class="social" aria-label="Social profiles">
      <span></span><span></span><span></span><span></span><span></span>
    </div>
    <p class="web"><svg viewBox="0 0 14 14"><circle cx="7" cy="7" r="6"/><ellipse cx="7" cy="7" rx="2.6" ry="6"/><line x1="1" y1="7" x2="13" y2="7"/></svg>www.<span class="accent">cedarharborhub</span>.com</p>
  </section>
</body>
</html>
```